International Education App needs UI Design

My current app is being upgraded and totally rebranded. This app is aimed to become No1. communication app for schools worldwide. Aimed at parents and high school students it will have events, assessments, messages, newsletters, notes, policies, contact us plus much more.
It will need to be much engaging and professional than all other apps on the market. You can see them attached to compare as well as the app logo to tie in the design. You can also see my current app and why needs an upgrade.
There will need to be design for each screen.
Needs a slick and professional finish with Tranvelo Blue as the base colour.
The app is called ClassNook
You will also find a file attached which shows functionality which will help design screens.

Target Market(s)

Parents, High Schools Students

Industry/Entity Type

Education

Font styles to use
Sans Serif

Colors
0355a3

Requirements
Must have
• Sleek, modern, professional and better than examples provided.
• I need a splash screen, home screen and each of the other screens designed.

```html
<!DOCTYPE html>
<html lang="en">
<head>
<meta charset="utf-8">
<title>ClassNook – Home</title>
<link rel="stylesheet" href="https://fonts.googleapis.com/css2?family=Open+Sans:wght@400;600&display=swap">
<style>
  :root {
    --brand-blue: #0355a3;
    --brand-blue-light: #0b63b8;
    --tab-active: #1a8fd8;
    --list-bg: #262626;
    --row-highlight: #4a4a4a;
    --row-divider: #3a3a3a;
    --icon-ring: #111418;
    --icon-fill: #1c2430;
    --icon-stroke: #8fa3b8;
    --text: #ffffff;
    --badge: #0355a3;
    --tabbar-bg: #1c1c1c;
    --tab-text: #d8d8d8;
  }
  * { box-sizing: border-box; margin: 0; padding: 0; }
  html, body { width: 1200px; height: 2352px; overflow: hidden; background: var(--list-bg); }
  body { font-family: "Open Sans", sans-serif; color: var(--text); position: relative; }

  .status-bar {
    height: 80px; background: var(--brand-blue);
    display: flex; align-items: center; justify-content: space-between;
    padding: 0 30px; font-size: 36px; font-weight: 600;
  }
  .status-bar .carrier { display: flex; align-items: center; gap: 14px; }
  .signal-dots { display: flex; gap: 6px; }
  .signal-dots span { width: 16px; height: 16px; border-radius: 50%; background: #fff; }
  .signal-dots span.off { background: transparent; border: 2px solid #fff; }
  .status-bar .battery { display: flex; align-items: center; gap: 14px; }
  .battery-icon { width: 70px; height: 32px; border: 3px solid #fff; border-radius: 5px; padding: 3px; position: relative; }
  .battery-icon::after { content: ""; position: absolute; right: -10px; top: 8px; width: 5px; height: 12px; background: #fff; border-radius: 0 2px 2px 0; }
  .battery-icon span { display: block; width: 100%; height: 100%; background: #fff; border-radius: 2px; }

  .nav-bar {
    height: 150px; background: linear-gradient(var(--brand-blue-light), var(--brand-blue));
    display: flex; align-items: center; justify-content: center; position: relative;
    font-size: 52px; font-weight: 400;
  }
  .menu-button { position: absolute; right: 40px; top: 50%; transform: translateY(-50%); width: 90px; }
  .menu-button span { display: block; height: 8px; background: #fff; margin: 14px 0; border-radius: 2px; }

  .menu-list { position: absolute; top: 230px; bottom: 200px; left: 0; right: 0; overflow: hidden; list-style: none; }
  .menu-item {
    height: 252px; display: flex; align-items: center; padding: 0 40px 0 36px;
    border-bottom: 3px solid var(--row-divider);
  }
  .menu-item.is-active { background: var(--row-highlight); }
  .menu-icon {
    width: 200px; height: 200px; border-radius: 50%; flex: none;
    background: var(--icon-fill); border: 8px solid var(--icon-ring);
    box-shadow: 0 0 0 3px #555 inset;
    display: flex; align-items: center; justify-content: center;
  }
  .menu-icon svg { width: 110px; height: 110px; }
  .menu-label { flex: 1; margin-left: 44px; font-size: 56px; font-weight: 400; }
  .menu-badge {
    width: 74px; height: 74px; border-radius: 50%; background: var(--badge);
    font-size: 36px; font-weight: 600; display: flex; align-items: center; justify-content: center;
    margin-right: 30px;
  }
  .menu-chevron { width: 44px; height: 80px; }

  .tab-bar {
    position: absolute; left: 0; right: 0; bottom: 0; height: 200px; background: var(--tabbar-bg);
    display: flex; border-top: 2px solid #333;
  }
  .tab { flex: 1; display: flex; flex-direction: column; align-items: center; justify-content: center; gap: 12px; font-size: 30px; color: var(--tab-text); }
  .tab svg { width: 86px; height: 86px; }
  .tab.is-active { background: var(--tab-active); color: #ffffff; }
</style>
</head>
<body>
  <header class="status-bar">
    <div class="carrier">
      <div class="signal-dots"><span></span><span></span><span></span><span class="off"></span><span class="off"></span></div>
      <span>VOLT</span>
      <svg width="40" height="32" viewBox="0 0 40 32"><path d="M4 12a24 24 0 0 1 32 0M10 18a15 15 0 0 1 20 0M16 24a6 6 0 0 1 8 0" fill="none" stroke="#fff" stroke-width="4" stroke-linecap="round"/></svg>
    </div>
    <div class="clock">4:21 PM</div>
    <div class="battery">
      <svg width="22" height="36" viewBox="0 0 22 36"><path d="M3 10l16 16-8 8V2l8 8L3 26" fill="none" stroke="#fff" stroke-width="3"/></svg>
      <span>100%</span>
      <div class="battery-icon"><span></span></div>
    </div>
  </header>

  <nav class="nav-bar">
    <h1 style="font-size:inherit;font-weight:inherit">Home</h1>
    <div class="menu-button" aria-label="Menu"><span></span><span></span><span></span></div>
  </nav>

  <ul class="menu-list">
    <li class="menu-item">
      <div class="menu-icon"><svg viewBox="0 0 100 100" fill="none" stroke="var(--icon-stroke)" stroke-width="6"><circle cx="50" cy="34" r="18"/><path d="M16 94c0-22 14-36 34-36s34 14 34 36"/></svg></div>
      <span class="menu-label">Students</span><span class="menu-badge">25</span>
      <svg class="menu-chevron" viewBox="0 0 44 80"><path d="M6 6l32 34-32 34" fill="none" stroke="#fff" stroke-width="6"/></svg>
    </li>
    <li class="menu-item is-active">
      <div class="menu-icon"><svg viewBox="0 0 100 100" fill="none" stroke="var(--icon-stroke)" stroke-width="6"><rect x="10" y="20" width="64" height="66" rx="4"/><path d="M10 36h64M26 12v14M58 12v14"/><text x="42" y="74" font-size="28" fill="var(--icon-stroke)" stroke="none" text-anchor="middle" font-family="Open Sans, sans-serif">12</text><circle cx="76" cy="30" r="16"/><path d="M69 30l5 5 9-10"/></svg></div>
      <span class="menu-label">Events</span><span class="menu-badge">2</span>
      <svg class="menu-chevron" viewBox="0 0 44 80"><path d="M6 6l32 34-32 34" fill="none" stroke="#fff" stroke-width="6"/></svg>
    </li>
    <li class="menu-item">
      <div class="menu-icon"><svg viewBox="0 0 100 100" fill="none" stroke="var(--icon-stroke)" stroke-width="6"><rect x="10" y="24" width="80" height="54" rx="4"/><path d="M10 26l40 30 40-30M10 78l30-26M90 78L60 52"/></svg></div>
      <span class="menu-label">Messages</span><span class="menu-badge">1</span>
      <svg class="menu-chevron" viewBox="0 0 44 80"><path d="M6 6l32 34-32 34" fill="none" stroke="#fff" stroke-width="6"/></svg>
    </li>
    <li class="menu-item">
      <div class="menu-icon"><svg viewBox="0 0 100 100" fill="none" stroke="var(--icon-stroke)" stroke-width="6"><rect x="18" y="16" width="68" height="70" rx="3"/><path d="M18 30H10v50a6 6 0 0 0 12 0M28 30h48M28 44h22v22H28zM58 46h18M58 58h18M28 74h48"/></svg></div>
      <span class="menu-label">Newsletters</span><span class="menu-badge">6</span>
      <svg class="menu-chevron" viewBox="0 0 44 80"><path d="M6 6l32 34-32 34" fill="none" stroke="#fff" stroke-width="6"/></svg>
    </li>
    <li class="menu-item">
      <div class="menu-icon"><svg viewBox="0 0 100 100" fill="none" stroke="var(--icon-stroke)" stroke-width="6"><rect x="14" y="14" width="62" height="74" rx="3"/><path d="M26 32h38M26 46h30M26 60h22M50 78l4-14 30-30 10 10-30 30z"/></svg></div>
      <span class="menu-label">Notes</span><span class="menu-badge">4</span>
      <svg class="menu-chevron" viewBox="0 0 44 80"><path d="M6 6l32 34-32 34" fill="none" stroke="#fff" stroke-width="6"/></svg>
    </li>
    <li class="menu-item">
      <div class="menu-icon"><svg viewBox="0 0 100 100" fill="none" stroke="var(--icon-stroke)" stroke-width="6"><path d="M30 62a18 18 0 0 1-4-34 24 24 0 0 1 48 0 18 18 0 0 1-4 34z"/><path d="M30 62v24h40V62M42 70v10M58 70v10"/></svg></div>
      <span class="menu-label">Canteen</span><span class="menu-badge">3</span>
      <svg class="menu-chevron" viewBox="0 0 44 80"><path d="M6 6l32 34-32 34" fill="none" stroke="#fff" stroke-width="6"/></svg>
    </li>
    <li class="menu-item">
      <div class="menu-icon"><svg viewBox="0 0 100 100" fill="none" stroke="var(--icon-stroke)" stroke-width="6"><rect x="12" y="20" width="72" height="66" rx="4"/><path d="M12 36h72M30 12v14M66 12v14M24 50h10M44 50h10M64 50h10M24 66h10M44 66h10"/></svg></div>
      <span class="menu-label">Calendar</span><span class="menu-badge">5</span>
      <svg class="menu-chevron" viewBox="0 0 44 80"><path d="M6 6l32 34-32 34" fill="none" stroke="#fff" stroke-width="6"/></svg>
    </li>
  </ul>

  <footer class="tab-bar">
    <div class="tab is-active">
      <svg viewBox="0 0 100 100"><path d="M50 8l12 28 30 3-23 20 7 30-26-16-26 16 7-30L8 39l30-3z" fill="none" stroke="#fff" stroke-width="5" stroke-linejoin="round"/></svg>
      <span>Featured</span>
    </div>
    <div class="tab">
      <svg viewBox="0 0 100 100" fill="none" stroke="var(--tab-text)" stroke-width="5"><rect x="20" y="10" width="60" height="80" rx="4"/><path d="M32 30h36M32 46h36M32 62h36M32 76h20"/></svg>
      <span>Top Charts</span>
    </div>
    <div class="tab">
      <svg viewBox="0 0 100 100" fill="none" stroke="var(--tab-text)" stroke-width="5"><circle cx="50" cy="32" r="12"/><path d="M50 20a12 12 0 0 1 0 0M28 68c4-14 40-14 44 0M14 90l14-26h44l14 26z"/></svg>
      <span>Near me</span>
    </div>
    <div class="tab">
      <svg viewBox="0 0 100 100" fill="none" stroke="var(--tab-text)" stroke-width="6"><circle cx="42" cy="42" r="26"/><path d="M62 62l26 26" stroke-linecap="round"/></svg>
      <span>Search</span>
    </div>
    <div class="tab">
      <svg viewBox="0 0 100 100" fill="none" stroke="var(--tab-text)" stroke-width="5"><path d="M14 50v36h72V50M50 12v52M32 46l18 18 18-18"/></svg>
      <span>Updates</span>
    </div>
  </footer>
</body>
</html>
```